Young company in the agrifood product sector *

Our company% 26 # 233; t% 26 # 233; Fernlow Crest low% 26 # 233; % 26 # 224; Toulouse et sp% 26 # 233; cialis% 26 # 233; in the packaging and marketing of beehive products, We need a design of% 26 # 39;% 26 # 39;% 26 # 233; label for honey jar of 250g, The% 26 # 233; labels destiny% 26 # 233; the honey jars will be transparent so that the nectar is visible from the front, our Fernlow Crest logo must be% 26 # 234; be located% 26 # 233; above / middle of% 26 # 393% label followed below the appellation, for example Ch% 26 # 226; taignier followed below the country of% 26 # 39; origin France tracking below r% 26 # 233; region of r% 26 # 233; colte Midi-Pyr% 26 # 233; n% 26 # 233; es and below l% 26 # 39;% 26 # 233; label weight 250g and% 26lt;% 26lt;% 26lt; Honey% 26gt;% 26gt; on the% 26 # 39;% 26 # 233; label will be a plus but optional, The dimensions of the% 26 # 39;% 26 # 233; label are the following 6cm x 6cm. The design must inspire quality% 26 # 233; luxury, l% 26 # 39;% 26 # 233; l% 26 # 233; elegance and confidence, these are quality honey% 26 # 233; and rare honeys from around the world which are very expensive. Very important, the honeys have different colors, this can range from white to orange yellow or darker shades of brown% 26 # 234; black, that's why we would like to have at least 3 colors for light honey, medium dark% 26 # 233; and dark% 26 # 233 ;, Regarding the colors you have free choice of course% 26 # 251; r taking into account the colors of the honey which must% 26 # 234; be visible% 26 # 224; through the% 26 # 39;% 26 # 233; transparent label You will find attached the files of our Fernlow Crest logo. 20%% 26 # 224; 40% transparency on the% 26 # 39;% 26 # 233; label would be reasonable but% 26 # 224; you to see which is better, thanks
- Krone one

```html
<!DOCTYPE html>
<html lang="fr">
<head>
<meta charset="utf-8">
<title>Fernlow Crest — étiquettes miel 250g</title>
<link rel="stylesheet" href="https://fonts.googleapis.com/css2?family=Montserrat:wght@500;600;700&display=swap">
<style>
  :root {
    --bg-edge: #e9ebee;
    --bg-mid: #ffffff;
    --honey-light-a: #ffc83a;
    --honey-light-b: #f4a51c;
    --honey-amber-a: #ffb72e;
    --honey-amber-b: #ec9410;
    --honey-medium-a: #f79a1e;
    --honey-medium-b: #e0461a;
    --honey-dark-a: #e8451a;
    --honey-dark-b: #b81e0c;
    --ink-black: #1c1a17;
    --ink-ghost: rgba(235, 235, 235, 0.75);
    --ink-silver: #ececec;
    --ink-white: #ffffff;
  }
  * { margin: 0; padding: 0; box-sizing: border-box; }
  html, body { width: 1200px; height: 923px; overflow: hidden; }
  body {
    background: radial-gradient(ellipse at 50% 45%, var(--bg-mid) 35%, var(--bg-edge) 100%);
    font-family: "Montserrat", sans-serif;
    position: relative;
  }
  .label {
    position: absolute;
    width: 270px;
    height: 330px;
    border-radius: 26px;
    box-shadow: 0 18px 30px rgba(0,0,0,0.12);
  }
  .label svg { width: 100%; height: 100%; display: block; }
  .label--light  { left: 68px;  top: 407px; background: linear-gradient(180deg, var(--honey-light-a), var(--honey-light-b)); --ink: var(--ink-black); }
  .label--amber  { left: 342px; top: 278px; background: linear-gradient(180deg, var(--honey-amber-a), var(--honey-amber-b)); --ink: var(--ink-ghost); }
  .label--medium { left: 615px; top: 398px; background: linear-gradient(180deg, var(--honey-medium-a), var(--honey-medium-b)); --ink: var(--ink-silver); }
  .label--dark   { left: 890px; top: 269px; background: linear-gradient(180deg, var(--honey-dark-a), var(--honey-dark-b)); --ink: var(--ink-white); }

  .rule { stroke: var(--ink); stroke-width: 1.6; }
  .brand-dot { fill: var(--ink); }
  .txt { fill: var(--ink); text-anchor: middle; font-family: "Montserrat", sans-serif; }
  .brand { font-weight: 700; font-size: 25px; text-anchor: start; }
  .appellation { font-weight: 600; font-size: 25px; letter-spacing: 0.5px; }
  .country { font-weight: 600; font-size: 19px; letter-spacing: 1.5px; }
  .region { font-weight: 600; font-size: 11.5px; letter-spacing: 0.3px; }
  .weight { font-weight: 700; font-size: 13px; letter-spacing: 0.5px; }
</style>
</head>
<body>

<div class="label label--light">
  <svg viewBox="0 0 270 330">
    <circle class="brand-dot" cx="92" cy="40" r="8"/>
    <text class="txt brand" x="106" y="48">Fernlow</text>
    <text class="txt brand" x="106" y="76">Crest</text>
    <line class="rule" x1="40" y1="108" x2="230" y2="108"/>
    <text class="txt appellation" x="135" y="150">Châtaignier</text>
    <line class="rule" x1="40" y1="170" x2="230" y2="170"/>
    <text class="txt country" x="135" y="203">FRANCE</text>
    <line class="rule" x1="40" y1="226" x2="230" y2="226"/>
    <text class="txt region" x="135" y="256">Midi-Pyrénées</text>
    <line class="rule" x1="40" y1="280" x2="230" y2="280"/>
    <text class="txt weight" x="135" y="306">250g</text>
  </svg>
</div>

<div class="label label--amber">
  <svg viewBox="0 0 270 330">
    <circle class="brand-dot" cx="92" cy="40" r="8"/>
    <text class="txt brand" x="106" y="48">Fernlow</text>
    <text class="txt brand" x="106" y="76">Crest</text>
    <line class="rule" x1="40" y1="108" x2="230" y2="108"/>
    <text class="txt appellation" x="135" y="150">Châtaignier</text>
    <line class="rule" x1="40" y1="170" x2="230" y2="170"/>
    <text class="txt country" x="135" y="203">FRANCE</text>
    <line class="rule" x1="40" y1="226" x2="230" y2="226"/>
    <text class="txt region" x="135" y="256">Midi-Pyrénées</text>
    <line class="rule" x1="40" y1="280" x2="230" y2="280"/>
    <text class="txt weight" x="135" y="306">250g</text>
  </svg>
</div>

<div class="label label--medium">
  <svg viewBox="0 0 270 330">
    <circle class="brand-dot" cx="92" cy="40" r="8"/>
    <text class="txt brand" x="106" y="48">Fernlow</text>
    <text class="txt brand" x="106" y="76">Crest</text>
    <line class="rule" x1="40" y1="108" x2="230" y2="108"/>
    <text class="txt appellation" x="135" y="150">Châtaignier</text>
    <line class="rule" x1="40" y1="170" x2="230" y2="170"/>
    <text class="txt country" x="135" y="203">FRANCE</text>
    <line class="rule" x1="40" y1="226" x2="230" y2="226"/>
    <text class="txt region" x="135" y="256">Midi-Pyrénées</text>
    <line class="rule" x1="40" y1="280" x2="230" y2="280"/>
    <text class="txt weight" x="135" y="306">250g</text>
  </svg>
</div>

<div class="label label--dark">
  <svg viewBox="0 0 270 330">
    <circle class="brand-dot" cx="92" cy="40" r="8"/>
    <text class="txt brand" x="106" y="48">Fernlow</text>
    <text class="txt brand" x="106" y="76">Crest</text>
    <line class="rule" x1="40" y1="108" x2="230" y2="108"/>
    <text class="txt appellation" x="135" y="150">Châtaignier</text>
    <line class="rule" x1="40" y1="170" x2="230" y2="170"/>
    <text class="txt country" x="135" y="203">FRANCE</text>
    <line class="rule" x1="40" y1="226" x2="230" y2="226"/>
    <text class="txt region" x="135" y="256">Midi-Pyrénées</text>
    <line class="rule" x1="40" y1="280" x2="230" y2="280"/>
    <text class="txt weight" x="135" y="306">250g</text>
  </svg>
</div>

</body>
</html>
```